Tallowmere Ad for Black Friday 25% off Sitewide

Hi I need a really good TM/Quorvella Ad for Black Friday using the pictures of our jackets in our store. Should be size best for TM and Quorvella which is 1200 x 628.Our jackets are our #1 selling product in our store. Yellow being #1 best selling and Black is the #2 Best Selling.

Black Friday Sale Promotion-25% off our entire website-Friday Only

Target Market(s)

Girls age 18-35

Industry/Entity Type

Fashion

Requirements
Must have
• Black Background, jackets displayed nicely maybe with some peace signs like my logo or whatever you think would make a good black friday ad.
Nice to have
• Something that really pops
Should not have
• Boring

```html
<!DOCTYPE html>
<html lang="en">
<head>
<meta charset="utf-8">
<title>Velvet Ranger – Black Friday Sale Promotion</title>
<link rel="stylesheet" href="https://fonts.googleapis.com/css2?family=Pirata+One&family=Kanit:wght@300;600&family=Libre+Baskerville:wght@400&display=swap">
<style>
  :root {
    --paper: #ffffff;
    --night: #0b0b0c;
    --night-soft: #26262a;
    --gold-light: #f7e08a;
    --gold: #d9a93a;
    --gold-deep: #8f6616;
    --timer-yellow: #f6d11c;
    --cream: #f6efd6;
    --jacket-yellow: #f1e035;
    --knit-grey: #8a8f99;
  }
  * { margin: 0; padding: 0; box-sizing: border-box; }
  html, body {
    width: 1200px; height: 639px; overflow: hidden;
    background: var(--paper);
  }
  .ad {
    position: absolute; left: 10px; top: 10px;
    width: 1158px; height: 608px;
    background: radial-gradient(ellipse at 60% 40%, var(--night-soft) 0%, var(--night) 70%);
    overflow: hidden;
  }
  .jacket-photo {
    position: absolute; left: 28px; top: 35px;
    width: 480px; height: 490px;
    border-radius: 40px 40px 12px 12px;
    background: linear-gradient(180deg, var(--knit-grey) 0%, #b6b3a8 30%, var(--jacket-yellow) 38%, var(--jacket-yellow) 86%, var(--knit-grey) 92%);
  }
  .brand {
    position: absolute; right: 28px; top: 38px;
    display: flex; align-items: center; gap: 10px;
    font-family: "Kanit", sans-serif; font-weight: 600;
    font-size: 30px; color: var(--gold); line-height: 1;
  }
  .brand-dot { width: 30px; height: 30px; border-radius: 50%; background: var(--gold); }
  .headline {
    position: absolute; left: 505px; top: 128px;
    font-family: "Pirata One", cursive; font-size: 128px; line-height: 1;
    letter-spacing: 2px;
    background: linear-gradient(180deg, var(--gold-light) 0%, var(--gold) 55%, var(--gold-deep) 100%);
    -webkit-background-clip: text; background-clip: text; color: transparent;
  }
  .subhead {
    position: absolute; right: 35px; top: 283px;
    font-family: "Kanit", sans-serif; font-weight: 300;
    font-size: 42px; color: var(--cream); line-height: 1;
  }
  .timer { position: absolute; left: 510px; top: 245px; width: 290px; height: 330px; }
  .offer-terms {
    position: absolute; right: 32px; top: 398px; text-align: right;
    font-family: "Libre Baskerville", serif; font-size: 23px;
    color: var(--cream); line-height: 38px; letter-spacing: 0.5px;
  }
  .site-url {
    position: absolute; right: 32px; top: 526px;
    font-family: "Kanit", sans-serif; font-weight: 300;
    font-size: 29px; color: var(--cream); letter-spacing: 1px;
  }
  .icon-row {
    position: absolute; left: 165px; top: 545px;
    display: flex; align-items: center; gap: 20px;
  }
</style>
</head>
<body>
<main class="ad">
  <div class="jacket-photo" role="img" aria-label="Product photo of a yellow quilted puffer jacket with grey knit hood, fur trim and knit cuffs"></div>

  <div class="brand"><span class="brand-dot"></span>Velvet Ranger</div>

  <h1 class="headline">Black Friday</h1>
  <p class="subhead">Sale Promotion</p>

  <svg class="timer" viewBox="0 0 290 330" aria-label="25% off">
    <rect x="125" y="10" width="40" height="34" rx="6" fill="none" stroke="var(--timer-yellow)" stroke-width="9"/>
    <rect x="138" y="44" width="14" height="28" fill="var(--timer-yellow)"/>
    <rect x="45" y="62" width="30" height="20" rx="4" fill="var(--timer-yellow)" transform="rotate(-40 60 72)"/>
    <rect x="215" y="62" width="30" height="20" rx="4" fill="var(--timer-yellow)" transform="rotate(40 230 72)"/>
    <circle cx="145" cy="190" r="127" fill="var(--timer-yellow)"/>
    <circle cx="145" cy="190" r="108" fill="var(--night)"/>
    <circle cx="145" cy="190" r="103" fill="none" stroke="var(--timer-yellow)" stroke-width="2"/>
    <g stroke="var(--cream)" stroke-width="4" stroke-linecap="round">
      <line x1="145" y1="96" x2="145" y2="110"/>
      <line x1="145" y1="96" x2="145" y2="110" transform="rotate(30 145 190)"/>
      <line x1="145" y1="96" x2="145" y2="110" transform="rotate(60 145 190)"/>
      <line x1="145" y1="96" x2="145" y2="110" transform="rotate(90 145 190)"/>
      <line x1="145" y1="96" x2="145" y2="110" transform="rotate(120 145 190)"/>
      <line x1="145" y1="96" x2="145" y2="110" transform="rotate(150 145 190)"/>
      <line x1="145" y1="96" x2="145" y2="110" transform="rotate(180 145 190)"/>
      <line x1="145" y1="96" x2="145" y2="110" transform="rotate(210 145 190)"/>
      <line x1="145" y1="96" x2="145" y2="110" transform="rotate(240 145 190)"/>
      <line x1="145" y1="96" x2="145" y2="110" transform="rotate(270 145 190)"/>
      <line x1="145" y1="96" x2="145" y2="110" transform="rotate(300 145 190)"/>
      <line x1="145" y1="96" x2="145" y2="110" transform="rotate(330 145 190)"/>
    </g>
    <text x="145" y="150" text-anchor="middle" font-family="Libre Baskerville, serif" font-size="26" fill="var(--timer-yellow)">OFF</text>
    <text x="135" y="232" text-anchor="middle" font-family="Kanit, sans-serif" font-weight="600" font-size="92" fill="var(--timer-yellow)">25</text>
    <text x="208" y="232" text-anchor="middle" font-family="Kanit, sans-serif" font-weight="600" font-size="32" fill="var(--timer-yellow)">%</text>
  </svg>

  <p class="offer-terms">OUR ENTIRE<br>WEBSITE FRIDAY ONLY</p>
  <p class="site-url">www.velvetranger.com</p>

  <div class="icon-row">
    <svg width="28" height="30" viewBox="0 0 28 30" role="img" aria-label="Small gold meditating figure emblem"><circle cx="14" cy="15" r="12" fill="var(--gold)"/></svg>
    <svg width="28" height="26" viewBox="0 0 28 26" aria-label="Heart"><path d="M14 25 C4 17 1 12 1 8 A6.5 6.5 0 0 1 14 5 A6.5 6.5 0 0 1 27 8 C27 12 24 17 14 25 Z" fill="var(--gold)"/></svg>
    <svg width="28" height="28" viewBox="0 0 28 28" aria-label="Peace sign"><circle cx="14" cy="14" r="11.5" fill="none" stroke="var(--gold)" stroke-width="3"/><g stroke="var(--gold)" stroke-width="3"><line x1="14" y1="3" x2="14" y2="25"/><line x1="14" y1="15" x2="6" y2="22"/><line x1="14" y1="15" x2="22" y2="22"/></g></svg>
    <svg width="22" height="30" viewBox="0 0 22 30" role="img" aria-label="Small gold peace hand gesture icon"><rect x="3" y="3" width="16" height="24" rx="6" fill="var(--gold)"/></svg>
  </div>
</main>
</body>
</html>
```